Business card - Harbourline Stoneworks

Design a business card utilizing the given logo.
colors we like: Black, greys, Teal, blues.
Tri color card, horizontal orientation likely
Logo and name likely best on top.
Info on card:

Dennis Farrowby
#5 - 4180 Maple Ridge Blvd.
Surrey, B.C. V3K 2R9

778.555.0193
dennisfarrowby@brellnet.ca

Slogan: "Building Dreams"

We are a construction company that specializes in new home construction on the West coast of BC Canada. Open Concepts designs of high end homes.

```html
<!DOCTYPE html>
<html lang="en">
<head>
<meta charset="utf-8">
<title>Harbourline Stoneworks – Business Card</title>
<link rel="stylesheet" href="https://fonts.googleapis.com/css2?family=Michroma&family=Arimo:wght@700&display=swap">
<style>
  :root{
    --stage:#2a2c2e;
    --card-black:#050505;
    --card-charcoal:#1b1b1b;
    --band-dark:#0c0c0c;
    --panel:#111111;
    --ink-white:#f2f2f2;
    --ink-grey:#c9c9c9;
    --ink-muted:#8a8a8a;
    --faint:#262626;
  }
  *{margin:0;padding:0;box-sizing:border-box}
  html,body{width:1200px;height:900px;overflow:hidden;background:var(--stage)}
  .canvas{position:relative;width:1200px;height:900px}
  .card{
    position:absolute;left:250px;width:700px;height:400px;overflow:hidden;
    background:linear-gradient(160deg,var(--card-charcoal) 0%,var(--card-black) 55%,#000 100%);
    box-shadow:0 12px 30px rgba(0,0,0,.55);
  }
  .card--front{top:35px}
  .card--back{top:465px}

  /* front */
  .front-band{position:absolute;top:0;bottom:0;left:470px;width:230px;
    background:linear-gradient(90deg,rgba(255,255,255,.04),rgba(0,0,0,.25))}
  .brand{position:absolute;left:70px;top:150px;display:flex;align-items:center;gap:22px}
  .brand__dot{width:70px;height:70px;border-radius:50%;border:3px solid var(--ink-white)}
  .brand__name{font-family:"Michroma",sans-serif;color:var(--ink-white);font-size:30px;line-height:1.15;letter-spacing:2px;text-transform:uppercase}
  .slogan{position:absolute;left:162px;top:265px;font-family:"Michroma",sans-serif;font-size:17px;letter-spacing:3px;color:var(--ink-grey);text-transform:uppercase}

  /* back */
  .back-band{position:absolute;top:0;bottom:0;left:0;width:170px;
    background:linear-gradient(180deg,#151515,#070707)}
  .back-mark{position:absolute;left:60px;top:120px;width:150px;height:150px;border-radius:50%;background:var(--faint);opacity:.7}
  .holder{position:absolute;left:285px;top:85px;font-family:"Michroma",sans-serif;color:var(--ink-white);font-size:24px;letter-spacing:4px;text-transform:uppercase}
  .contact{position:absolute;left:255px;top:135px;width:445px;height:170px;background:var(--panel);
    box-shadow:inset 0 0 0 1px #1f1f1f;display:flex}
  .contact__icons{width:85px;position:relative}
  .contact__icons svg{position:absolute;left:30px;fill:none;stroke:var(--ink-muted);stroke-width:1.6}
  .contact__lines{padding-top:14px;font-family:"Arimo",sans-serif;font-weight:700;font-size:19px;line-height:30px;color:var(--ink-grey);list-style:none}
</style>
</head>
<body>
<main class="canvas">
  <section class="card card--front" aria-label="Card front">
    <div class="front-band"></div>
    <div class="brand">
      <span class="brand__dot"></span>
      <span class="brand__name">Harbourline<br>Stoneworks</span>
    </div>
    <p class="slogan">Building Dreams</p>
  </section>

  <section class="card card--back" aria-label="Card back">
    <div class="back-band"></div>
    <span class="back-mark"></span>
    <h1 class="holder">Dennis Farrowby</h1>
    <div class="contact">
      <div class="contact__icons">
        <svg style="top:22px" width="18" height="24" viewBox="0 0 18 24" aria-hidden="true"><rect x="2" y="3" width="14" height="20"/><path d="M6 7h2M10 7h2M6 11h2M10 11h2M6 15h2M10 15h2M8 23v-4h2v4"/></svg>
        <svg style="top:82px" width="18" height="24" viewBox="0 0 18 24" aria-hidden="true"><rect x="2" y="1" width="14" height="22" rx="2"/><path d="M7 19h4"/></svg>
        <svg style="top:122px" width="20" height="18" viewBox="0 0 20 18" aria-hidden="true"><rect x="1" y="1" width="18" height="12"/><path d="M7 17h6M10 13v4"/></svg>
      </div>
      <ul class="contact__lines">
        <li>#5 - 4180 Maple Ridge Blvd.</li>
        <li>Surrey, B.C. V3K 2R9</li>
        <li>778.555.0193</li>
        <li>dennisfarrowby@brellnet.ca</li>
      </ul>
    </div>
  </section>
</main>
</body>
</html>
```